Fatigued and Overloaded by COVID Messages? We need original illustrations to show that.

Everywhere you look there are messages about COVID. That is leading many people to feel fatigued and overloaded by the messages.

We surveyed U.S. adults March 20th - 24th, 2020 and measured message fatigue, information overload, perceived repetition, and perceived exaggeration. Here is how participants responded:

When it comes to coronavirus . . .
55% feel exhausted by all the messages.
54% feel overloaded by the amount of information.
51% feel that the messages are repetitive.
47% feel like messages exaggerate how bad it is.

In other words, almost half of U.S. adults show signs of message fatigue, information overload, perceived message repetition, and perceived message exaggeration.

We will continue to survey 400 adults every week for the next 16 weeks. Each time we will measure message fatigue, information overload, perceived repetition, and perceived exaggeration. We expect that it will increase over time.

What are we looking for? We need innovative and original illustrations that attempt to communicate these findings. The illustrations would visualize message fatigue, information overload, perceived message repetition, and perceived message exaggeration.

What sort of visual are we looking for? Our preference is for an original illustration (or set of illustrations). Our preference is for creative and powerful illustrations, but we are also open to the creative and well-executed infographics.

We need these images fast . We will award monetary prizes to the 3 best designs. If we like more than that, then we might purchase more (e.g., in past contests, we have purchased as many as 30 designs).

What we will need:
(1) The illustrations must be original and we will need the photoshop and/or illustrator files for all artwork. (By original, we mean that the illustrations are 100% created by you. Our organization requires that we utilize only original illustrated work. We have had issues with free imagery being pirated and reposted as free. We sidestep that issue by just having everything created.)

(2) The illustration should say, somewhere: "Based on a survey of 400 U.S. adults conducted March 20 - 24th, 2020."

(3) We will have almost 4 months worth of data by the time this is done. In other words, the illustrations might be able to help us present that weekly data.

(4) We have conducted other Artvendo projects. It might be helpful to examine designs we liked in the past. For example, here is another COVID project we just finished:

https://jobs.artvendo-example.com/job/5162048

Target Market(s)

U.S. adults

Requirements
Must have
• Original illustrations. Mobile friendly design. People will view this on their smartphones.
Nice to have
• A design that we can use to communicate the data across time.

```html
<!DOCTYPE html>
<html lang="en">
<head>
<meta charset="utf-8">
<title>COVID Message Fatigue Survey</title>
<link rel="stylesheet" href="https://fonts.googleapis.com/css2?family=Rubik:wght@500;700;900&family=Roboto:ital,wght@0,400;0,500;1,400;1,500&display=swap">
<style>
  :root {
    --navy: #4a4c7d;
    --coral: #ef6a6c;
    --yellow: #ffd54a;
    --red: #e8333a;
    --white: #ffffff;
    --ink: #3a3c66;
  }
  * { box-sizing: border-box; margin: 0; padding: 0; }
  html, body { width: 1200px; height: 3596px; overflow: hidden; }
  body {
    position: relative;
    background: var(--navy);
    font-family: "Roboto", Arial, sans-serif;
    color: var(--white);
  }
  .header-virus {
    position: absolute; right: -150px; top: -170px;
    width: 520px; height: 520px; border-radius: 50%;
    background: radial-gradient(circle at 40% 60%, #ffe06b, var(--yellow) 60%, #f7c43a);
  }
  .title {
    position: absolute; left: 100px; top: 90px; width: 820px;
    font-family: "Rubik", Arial, sans-serif; font-weight: 900;
    font-size: 84px; line-height: 1.08; letter-spacing: -1px;
  }
  .title .accent { color: var(--yellow); }
  .bubble {
    position: absolute; left: 210px; top: 460px; width: 720px; height: 180px;
    background: var(--yellow); border-radius: 14px;
    padding: 32px 60px 0 50px;
    font-style: italic; font-weight: 500; font-size: 38px; line-height: 1.2;
    color: var(--ink);
  }
  .bubble::after {
    content: ""; position: absolute; left: 60px; bottom: -40px;
    border-right: 50px solid transparent;
    border-top: 42px solid var(--yellow);
  }
  .bubble-alert {
    position: absolute; right: -36px; top: -48px;
    width: 96px; height: 96px; border-radius: 50%;
    background: var(--red); color: var(--white);
    font-family: "Rubik", Arial, sans-serif; font-weight: 900; font-size: 64px;
    display: flex; align-items: center; justify-content: center; font-style: normal;
  }
  .survey-note {
    position: absolute; left: 100px; top: 800px; width: 960px;
    font-style: italic; font-size: 32px; line-height: 1.3;
  }
  .lead {
    position: absolute; left: 100px; top: 990px; width: 1000px;
    font-family: "Rubik", Arial, sans-serif; font-weight: 700;
    font-size: 44px; line-height: 1.2;
  }
  .stats {
    position: absolute; left: 60px; top: 1188px; width: 1080px; height: 1780px;
    background: var(--white);
  }
  .tile {
    position: absolute; width: 456px; height: 820px;
    text-align: center; padding: 0 24px;
  }
  .tile--navy { background: var(--navy); }
  .tile--coral { background: var(--coral); }
  .tile-1 { left: 60px; top: 60px; }
  .tile-2 { left: 564px; top: 60px; }
  .tile-3 { left: 60px; top: 920px; }
  .tile-4 { left: 564px; top: 920px; }
  .tile-icon {
    width: 280px; height: 280px; border-radius: 50%;
    margin: 52px auto 0;
    background: radial-gradient(circle, rgba(255,255,255,0.95) 45%, rgba(255,255,255,0.75));
  }
  .tile-bar {
    width: 230px; height: 14px; margin: 148px auto 0;
    background: var(--yellow);
  }
  .tile-value {
    margin-top: 14px;
    font-family: "Rubik", Arial, sans-serif; font-weight: 900;
    font-size: 186px; line-height: 1; letter-spacing: -2px;
  }
  .tile-label {
    margin-top: 20px; font-size: 32px; line-height: 1.2;
  }
  .summary-map {
    position: absolute; left: 72px; top: 3010px; width: 440px; height: 220px;
    border-radius: 30px 60px 40px 80px; background: var(--white);
  }
  .summary-note {
    position: absolute; left: 72px; top: 3350px; width: 470px;
    font-style: italic; font-size: 21px; line-height: 1.3;
  }
  .summary {
    position: absolute; left: 580px; top: 3070px; width: 580px;
    font-family: "Rubik", Arial, sans-serif; font-weight: 700;
  }
  .summary-kicker { font-size: 30px; line-height: 1.1; }
  .summary-figure {
    font-weight: 900; font-size: 82px; line-height: 1; margin-top: 6px;
    white-space: nowrap; letter-spacing: -1px;
  }
  .summary-sub { font-size: 30px; margin-top: 8px; line-height: 1.1; }
  .signs { list-style: none; margin-top: 22px; width: 540px; }
  .sign {
    display: flex; align-items: center; height: 48px; margin-bottom: 14px;
    background: var(--white); color: var(--ink); border-radius: 24px;
    font-family: "Roboto", Arial, sans-serif; font-weight: 500; font-size: 25px;
    padding-left: 12px; white-space: nowrap;
  }
  .sign-num {
    flex: none; width: 30px; height: 30px; margin-right: 20px;
    border: 2px solid var(--ink); border-radius: 4px;
    display: flex; align-items: center; justify-content: center; font-size: 20px;
  }
</style>
</head>
<body>
  <div class="header-virus" role="img" aria-label="Illustration of a yellow coronavirus particle"></div>

  <h1 class="title">Everywhere you l<span class="accent">oo</span>k there are messages about COVID.</h1>

  <p class="bubble">That is leading many people to feel fatigued and overloaded by the messages.
    <span class="bubble-alert">!</span>
  </p>

  <p class="survey-note">We surveyed U.S. adults March 20th - 24th, 2020 and measured message fatigue, information overload, perceived repetition, and perceived exaggeration.</p>

  <h2 class="lead">Here is How Participants Responded:<br>When It Comes To Coronavirus . . .</h2>

  <section class="stats">
    <article class="tile tile--navy tile-1">
      <div class="tile-icon" role="img" aria-label="Illustration of a virus surrounded by message notifications"></div>
      <div class="tile-bar"></div>
      <div class="tile-value">55%</div>
      <p class="tile-label">feel exhausted by all<br>the messages.</p>
    </article>
    <article class="tile tile--coral tile-2">
      <div class="tile-icon" role="img" aria-label="Illustration of a virus covered in news pages and documents"></div>
      <div class="tile-bar"></div>
      <div class="tile-value">54%</div>
      <p class="tile-label">feel overloaded by the<br>amount of information.</p>
    </article>
    <article class="tile tile--coral tile-3">
      <div class="tile-icon" role="img" aria-label="Illustration of a virus with repeating chat message bubbles"></div>
      <div class="tile-bar"></div>
      <div class="tile-value">51%</div>
      <p class="tile-label">feel that the messages<br>are repetitive.</p>
    </article>
    <article class="tile tile--navy tile-4">
      <div class="tile-icon" role="img" aria-label="Illustration of a virus with an alert envelope and warning signs"></div>
      <div class="tile-bar"></div>
      <div class="tile-value">47%</div>
      <p class="tile-label">feel like messages<br>exaggerate how bad it is.</p>
    </article>
  </section>

  <div class="summary-map" role="img" aria-label="Map of the United States"></div>
  <p class="summary-note">We will continue to survey 400 adults every week for the next 16 weeks. Each time we will measure message fatigue, information overload, perceived repetition, and perceived exaggeration. We expect that it will increase over time.</p>

  <section class="summary">
    <p class="summary-kicker">IN OTHER WORDS</p>
    <p class="summary-figure">ALMOST 50%</p>
    <p class="summary-sub">OF U.S. ADULTS SHOW SIGNS OF</p>
    <ol class="signs">
      <li class="sign"><span class="sign-num">1</span>Message Fatigue</li>
      <li class="sign"><span class="sign-num">2</span>Information Overload</li>
      <li class="sign"><span class="sign-num">3</span>Perceived Message Repetition, and</li>
      <li class="sign"><span class="sign-num">4</span>Perceived Message Exaggeration</li>
    </ol>
  </section>
</body>
</html>
```